Copperleaf Motorized Shade Business Card

Hello, we've had our logo made. Now we are looking for a clean and cool looking business card. One side can just be the logo with any design elements that might look good with it. The other side will be Name, Phone Number and Email. There will not be an address on the card.

```html
<!DOCTYPE html>
<html lang="en">
<head>
<meta charset="UTF-8">
<title>Copperleaf Motorized Shade – Business Card</title>
<link rel="stylesheet" href="https://fonts.googleapis.com/css2?family=Oswald:wght@500;600&family=Montserrat:wght@300;400&display=swap">
<style>
  :root {
    --stage: #1e1e1e;
    --navy: #0e3c78;
    --sky: #1ba7e8;
    --paper: #ffffff;
    --ink: #4a4a4a;
  }
  * { margin: 0; padding: 0; box-sizing: border-box; }
  html, body {
    width: 1200px; height: 900px; overflow: hidden;
    background: var(--stage);
  }
  .card {
    position: absolute;
    left: 280px;
    width: 640px; height: 366px;
    overflow: hidden;
  }
  .card--back { top: 50px; background: var(--navy); }
  .card--front { top: 484px; background: var(--paper); }

  .back-brand {
    position: absolute; inset: 0;
    display: flex; flex-direction: column; align-items: center; justify-content: center;
    color: var(--paper);
    font-family: "Oswald", sans-serif; font-weight: 600;
  }
  .back-brand__name { font-size: 72px; letter-spacing: 2px; line-height: 1; }
  .back-brand__tag { font-size: 17px; letter-spacing: 9px; margin-top: 8px; }

  .front-brand {
    position: absolute; left: 44px; top: 38px;
    display: flex; align-items: center; gap: 16px;
    color: var(--navy);
    font-family: "Oswald", sans-serif; font-weight: 600;
  }
  .front-brand__square { width: 54px; height: 54px; background: var(--navy); }
  .front-brand__text { display: flex; flex-direction: column; }
  .front-brand__name { font-size: 58px; line-height: 1; letter-spacing: 1px; }
  .front-brand__tag { font-size: 15px; letter-spacing: 8px; margin-top: 6px; }

  .name-band {
    position: absolute; left: 0; right: 0; top: 190px; height: 50px;
    background: var(--navy);
    display: flex; align-items: center; padding-left: 44px;
    font-family: "Oswald", sans-serif; font-weight: 500; font-size: 36px;
    letter-spacing: 0.5px;
  }
  .name-band__first { color: var(--paper); margin-right: 8px; }
  .name-band__last { color: var(--sky); }

  .contact {
    position: absolute; left: 44px; top: 268px;
    font-family: "Montserrat", sans-serif; font-weight: 300; color: var(--ink);
    list-style: none;
  }
  .contact__item { display: flex; align-items: center; gap: 12px; margin-bottom: 10px; }
  .contact__item--phone { font-size: 28px; }
  .contact__item--email { font-size: 20px; }
  .contact__icon { width: 22px; height: 22px; flex: none; }
</style>
</head>
<body>
  <section class="card card--back" aria-label="Card back">
    <div class="back-brand">
      <span class="back-brand__name">COPPERLEAF</span>
      <span class="back-brand__tag">MOTORIZED SHADES</span>
    </div>
  </section>

  <section class="card card--front" aria-label="Card front">
    <div class="front-brand">
      <span class="front-brand__square"></span>
      <div class="front-brand__text">
        <span class="front-brand__name">COPPERLEAF</span>
        <span class="front-brand__tag">MOTORIZED SHADES</span>
      </div>
    </div>

    <div class="name-band">
      <span class="name-band__first">DANIEL</span>
      <span class="name-band__last">HARPER</span>
    </div>

    <ul class="contact">
      <li class="contact__item contact__item--phone">
        <svg class="contact__icon" viewBox="0 0 24 24" aria-hidden="true">
          <path fill="#0e3c78" d="M6.6 10.8a15.1 15.1 0 0 0 6.6 6.6l2.2-2.2a1 1 0 0 1 1-.25 11.4 11.4 0 0 0 3.6.57 1 1 0 0 1 1 1V20a1 1 0 0 1-1 1A17 17 0 0 1 3 4a1 1 0 0 1 1-1h3.5a1 1 0 0 1 1 1c0 1.25.2 2.45.57 3.57a1 1 0 0 1-.25 1z"/>
        </svg>
        <span>555. 014. 2238</span>
      </li>
      <li class="contact__item contact__item--email">
        <svg class="contact__icon" viewBox="0 0 24 24" aria-hidden="true">
          <rect x="2" y="5" width="20" height="14" rx="1.5" fill="none" stroke="#0e3c78" stroke-width="2"/>
          <path d="M3 6l9 7 9-7" fill="none" stroke="#0e3c78" stroke-width="2"/>
        </svg>
        <span>hello@copperleafshade.com</span>
      </li>
    </ul>
  </section>
</body>
</html>
```